Website Design: Business to Business Coaching/Strategy

DO NOT CONTACT ME PRIVATELY. ANY PRIVATE CONTACT WILL BE IGNORED.

I need a website design for a business to business coaching service.

The website is for a company the specializes in coaching/training for other businesses. The business specializes in business development and human resource management.

Where appropriate, please include calls to action, e.g.: book a service & request a quote

CONTENT (SEEE ATTACHMENT)
5 Pages;
1. Home Page with overview of company/services -> Slide show at the top with tagline:

WE HELP MAKE STRATEGY HAPPEN BY

DELIVERING LONG-TERM PERFORMANCE IMPROVEMENTS

SO COMPANIES CAN

"BECOME THE CHANGE THEY WISH TO SEE."

2. Works - core services; coaching; leadership development, workshops
3. Expertise
a. capability: helping people to help themselves
b. company interventions: working in partnership; team facilitation; …
c. testimonials
4. About Us
5. Inquires
a. business capability development and funding
b. Register / enrol for an open programme or workshop
c. client feedback

The website below provides services that are similar to the services of my company: https://www.velmoria.co.uk

DESIGN
- Dark theme matching this style of website BUT a simpler more straightforward design: https://www.hadlowcrest.ac.uk/
Another theme that I like - Dark themed with a modern/easy design: https://quorbastyles.com/theme-demos/?demo=lumetra-dark

Target Market(s)

Small businesses

Industry/Entity Type

Executive training/business coaching

Number of Pages Required

5+ page

Colors

Designer to choose colors to be used in the design.

```html
<!DOCTYPE html>
<html lang="en">
<head>
<meta charset="utf-8">
<title>Orivane Enterprise — Business Coaching &amp; Strategy</title>
<link rel="stylesheet" href="https://fonts.googleapis.com/css2?family=Jost:wght@300;400;500&family=Oswald:wght@400&family=Montserrat:wght@400;500&display=swap">
<style>
:root{
  --ink:#0a0909;
  --panel:#1c1c1e;
  --card:#202022;
  --orange:#ff6a25;
  --white:#ffffff;
  --soft:#d8d8d8;
  --line:#cfcfcf;
}
*{box-sizing:border-box;margin:0;padding:0}
html,body{width:1200px;height:4222px;overflow:hidden}
body{background:var(--ink);color:var(--white);font-family:"Jost",sans-serif;position:relative}
.abs{position:absolute}
a{color:inherit;text-decoration:none}

/* hero */
.hero-photo{left:194px;top:0;width:1006px;height:530px;background:linear-gradient(120deg,#6b6b6b 0%,#8a817a 35%,#b9aea4 60%,#6c6560 100%)}
.hero-photo::after{content:"";position:absolute;inset:0;background:linear-gradient(90deg,rgba(0,0,0,.55),rgba(0,0,0,.15) 70%)}
.brand{left:93px;top:28px;width:268px;height:51px;background:var(--ink);font-size:24px;font-weight:400;display:flex;align-items:center;padding-left:17px;letter-spacing:.3px}
.nav{top:40px;font-size:17px;font-weight:300}
.btn-solid{background:var(--orange);color:var(--white);font-size:16px;font-weight:400;display:flex;align-items:center;justify-content:center}
.btn-line{border:1.5px solid var(--line);color:var(--white);font-size:16px;font-weight:300;display:flex;align-items:center;justify-content:center}
.tagline{left:279px;top:190px;width:760px;font-size:32px;line-height:42px;font-weight:300}
.slide-dot{left:137px;width:5px;height:5px;border-radius:50%;background:var(--orange)}

/* side labels */
.side-label{left:28px;width:33px;border:1.5px solid var(--orange);display:flex;align-items:center;justify-content:center}
.side-label span{transform:rotate(-90deg);white-space:nowrap;font-family:"Oswald",sans-serif;font-size:13px;color:var(--orange);letter-spacing:.5px}

/* about */
.about-title{left:279px;top:628px;font-size:33px;line-height:38px;font-weight:300}
.about-copy{left:638px;top:628px;width:430px;font-family:"Montserrat",sans-serif;font-size:14.5px;line-height:26px}

/* services */
.services{left:0;top:905px;width:1200px;height:1319px;background:var(--panel)}
.photo{background:linear-gradient(135deg,#cfd3d8,#8c9199)}
.svc-title{font-size:28px;font-weight:300;letter-spacing:.3px}
.svc-copy{width:450px;font-family:"Montserrat",sans-serif;font-size:13.5px;line-height:21px;color:var(--soft)}
.plus{width:18px;height:18px;background:var(--orange);display:flex;align-items:center;justify-content:center;font-size:14px;line-height:1;color:var(--white)}

/* approach band */
.approach{left:0;top:2348px;width:1200px;height:219px;background:var(--orange)}
.approach h2{position:absolute;left:108px;top:60px;font-size:33px;font-weight:300}
.approach p{position:absolute;left:108px;top:110px;width:700px;font-size:18px;line-height:22px;font-weight:300}

/* works */
.work-circle{top:2657px;width:180px;height:180px;border-radius:50%}
.work-label{top:2862px;width:200px;text-align:center;font-size:18px;line-height:21px;font-weight:300}

/* expertise */
.expertise-card{left:446px;top:3147px;width:643px;height:387px;background:var(--card);padding:58px 0 0 84px}
.expertise-card h2{font-size:36px;font-weight:300;margin-bottom:14px}
.expertise-card p{font-size:19px;line-height:22px;font-weight:300;width:415px}
.expertise-list{list-style:none;margin-top:20px}
.expertise-list li{font-size:18px;font-weight:500;line-height:32px;display:flex;align-items:center;gap:14px}

/* footer */
.footer{left:0;top:3695px;width:1033px;height:527px;background:var(--panel)}
.foot-title{font-size:28px;font-weight:300}
.contact-row{left:108px;display:flex;align-items:flex-start;gap:12px;font-family:"Montserrat",sans-serif}
.field{left:530px;width:475px;background:var(--white);color:#333;font-family:"Montserrat",sans-serif;font-size:12.5px;padding:9px 16px}
.small-link{font-family:"Montserrat",sans-serif;font-size:13px;color:var(--soft)}
.social{left:1053px;width:32px;height:32px;border:1.5px solid var(--orange);display:flex;align-items:center;justify-content:center}
.social i{width:8px;height:8px;border-radius:50%;background:var(--orange);display:block}
.social.active{background:var(--orange)}
.social.active i{background:var(--white)}
</style>
</head>
<body>

<!-- Hero -->
<div class="abs hero-photo" role="img" aria-label="Photo of a young professional working on a laptop with colleagues at a meeting table"></div>
<div class="abs brand">Orivane Enterprise</div>
<a class="abs nav" style="left:506px">Home</a>
<a class="abs nav" style="left:604px">Works</a>
<a class="abs nav" style="left:705px">Expertise</a>
<a class="abs nav" style="left:830px">About Us</a>
<a class="abs btn-solid" style="left:948px;top:30px;width:141px;height:45px">Contact Us</a>

<h1 class="abs tagline">We help make strategy happen by<br>delivering long-term performance improvements<br>so companies can<br>"Become the change they wish to see."</h1>
<a class="abs btn-line" style="left:279px;top:395px;width:157px;height:43px">Book a Service</a>

<div class="abs slide-dot" style="top:390px"></div>
<div class="abs slide-dot" style="top:423px"></div>
<div class="abs slide-dot" style="top:455px"></div>
<svg class="abs" style="left:127px;top:477px" width="26" height="26" viewBox="0 0 26 26"><rect x="6" y="6" width="14" height="14" transform="rotate(45 13 13)" fill="none" stroke="#ff6a25" stroke-width="1.5"/><circle cx="13" cy="13" r="2.5" fill="#ff6a25"/></svg>

<svg class="abs" style="left:565px;top:496px" width="68" height="68" viewBox="0 0 68 68"><rect x="14" y="14" width="40" height="40" transform="rotate(45 34 34)" fill="#ff6a25"/><path d="M34 27v13M29 35l5 5 5-5" fill="none" stroke="#fff" stroke-width="1.8"/></svg>

<!-- About -->
<div class="abs side-label" style="top:617px;height:159px"><span>ABOUT US</span></div>
<h2 class="abs about-title">Welcome to<br>Orivane Enterprise</h2>
<p class="abs about-copy">Orivane Enterprise specialise in helping clients make strategy happen by delivering &nbsp;long-term performance improvements so they can "become the change they wish to see."</p>
<a class="abs btn-line" style="left:638px;top:774px;width:159px;height:41px">Discover More</a>

<!-- Services -->
<div class="abs services"></div>
<div class="abs side-label" style="top:967px;height:159px"><span>SERVICES</span></div>

<div class="abs photo" style="left:110px;top:872px;width:475px;height:353px" role="img" aria-label="Photo of a consultant presenting at a whiteboard to a team"></div>
<h3 class="abs svc-title" style="left:638px;top:963px">Leadership &amp; Ccpability</h3>
<p class="abs svc-copy" style="left:638px;top:1020px">There is a pressing need for leadership to be distributed across organisations in support of constant innovation and change. For businesses that believe there is a &nbsp;benefit in investing in their core resource – people, we can help you gain...</p>
<svg class="abs" style="left:636px;top:1142px" width="22" height="22" viewBox="0 0 22 22"><rect x="4" y="4" width="14" height="14" transform="rotate(45 11 11)" fill="#ff6a25"/><path d="M11 7v8M7 11h8" stroke="#fff" stroke-width="1.4"/></svg>
<span class="abs" style="left:672px;top:1143px;font-family:Montserrat,sans-serif;font-size:13px">Learn More</span>

<h3 class="abs svc-title" style="left:108px;top:1302px">Assessment &amp; Analysis</h3>
<p class="abs svc-copy" style="left:108px;top:1358px">We engage key stakeholders to identify issues, clarify direction and to have conversations about those areas that really matter. We help clients to commit to action, implement new business strategies, plan for the future and...</p>
<div class="abs plus" style="left:110px;top:1474px">+</div>
<div class="abs photo" style="left:613px;top:1253px;width:476px;height:298px;background:linear-gradient(135deg,#2a3b55,#c9ced6 55%,#e8e9eb)" role="img" aria-label="Photo of hands reviewing charts and reports on a desk"></div>

<div class="abs photo" style="left:110px;top:1579px;width:475px;height:351px;background:linear-gradient(135deg,#8a5a46,#b8aaa0 50%,#5d5a5c)" role="img" aria-label="Photo of a team seated in a circle during a workshop in a brick-walled office"></div>
<h3 class="abs svc-title" style="left:638px;top:1649px">People &amp; Engagement</h3>
<p class="abs svc-copy" style="left:638px;top:1706px">It's all about people; that is, the right people. Having leaders with an ability to facilitate the fulfilment of your company's purpose through your people provides potential for it to &nbsp;become ...</p>
<div class="abs plus" style="left:638px;top:1830px">+</div>

<h3 class="abs svc-title" style="left:108px;top:1988px">Investigate &amp; Guid</h3>
<p class="abs svc-copy" style="left:108px;top:2044px">Success in bussiness hinges on strategic agility as well as an ability to highlight and execute actions leading to measurable improvements. To help businesses to do this we will support, guide and partner with clients to assess ...</p>
<div class="abs plus" style="left:110px;top:2160px">+</div>
<div class="abs photo" style="left:613px;top:1960px;width:476px;height:298px;background:linear-gradient(135deg,#3a3d44,#8d9098 50%,#4a4c52)" role="img" aria-label="Photo of two business people shaking hands"></div>

<!-- Approach -->
<section class="abs approach">
  <h2>A Personalised Approach</h2>
  <p>Working in partnership we will learn about your business and your challenges<br>for the &nbsp;purpose of designing a programme appropriate to your situation.</p>
  <a class="abs btn-line" style="left:922px;top:87px;width:167px;height:45px;border-color:#fff">Book a Service</a>
</section>

<!-- Works -->
<div class="abs side-label" style="top:2657px;height:157px"><span>WORKS</span></div>
<div class="abs work-circle" style="left:110px;background:radial-gradient(circle,#8a7468,#3b3330)" role="img" aria-label="Photo of colleagues discussing around a table"></div>
<div class="abs work-circle" style="left:310px;background:radial-gradient(circle,#e4e1dc,#9b9690)" role="img" aria-label="Photo of a desk with charts and glasses"></div>
<div class="abs work-circle" style="left:510px;background:radial-gradient(circle,#5f6570,#262a31)" role="img" aria-label="Photo of a team planning over documents"></div>
<div class="abs work-circle" style="left:709px;background:radial-gradient(circle,#a39a84,#4a4538)" role="img" aria-label="Photo of a calculator and paperwork"></div>
<div class="abs work-circle" style="left:909px;background:radial-gradient(circle,#8c7c70,#3a332e)" role="img" aria-label="Photo of a person working at a desk"></div>
<div class="abs work-label" style="left:100px">People &amp;<br>Change</div>
<div class="abs work-label" style="left:300px">Organisation<br>Performance</div>
<div class="abs work-label" style="left:500px">Strategy &amp;<br>Direction</div>
<div class="abs work-label" style="left:699px">Sustainability</div>
<div class="abs work-label" style="left:899px">Operations &amp;<br>Risk</div>
<a class="abs btn-solid" style="left:521px;top:2944px;width:158px;height:44px">Contact Us</a>

<!-- Expertise -->
<div class="abs photo" style="left:110px;top:3077px;width:475px;height:528px;background:linear-gradient(135deg,#d8d6d2,#8a7a6e 55%,#3e3632)" role="img" aria-label="Photo of a workshop with a presenter at a flip chart and attendees using laptops"></div>
<section class="abs expertise-card">
  <h2>Expertise</h2>
  <p>For leaders who believe focused development<br>presents a competitive edge.</p>
  <ul class="expertise-list">
    <li><svg width="16" height="10" viewBox="0 0 16 10"><path d="M0 5h14M10 1l4 4-4 4" fill="none" stroke="#fff" stroke-width="1.5"/></svg>Coaching &amp; Mentoring</li>
    <li><svg width="16" height="10" viewBox="0 0 16 10"><path d="M0 5h14M10 1l4 4-4 4" fill="none" stroke="#fff" stroke-width="1.5"/></svg>Leadership</li>
    <li><svg width="16" height="10" viewBox="0 0 16 10"><path d="M0 5h14M10 1l4 4-4 4" fill="none" stroke="#fff" stroke-width="1.5"/></svg>Training &amp; Development</li>
  </ul>
  <a class="abs btn-line" style="left:84px;top:299px;width:157px;height:41px">Register Now</a>
</section>

<!-- Footer -->
<div class="abs footer"></div>
<div class="abs side-label" style="top:3756px;height:159px"><span>CONTACT US</span></div>

<h3 class="abs foot-title" style="left:108px;top:3752px">Orivane Enterprise</h3>
<div class="abs contact-row" style="top:3824px;font-size:20px;font-family:Jost,sans-serif;font-weight:300">
  <svg width="16" height="16" viewBox="0 0 16 16" style="margin-top:6px"><path d="M3 1l3 0 1.5 3.5-2 1.3a8 8 0 0 0 4.7 4.7l1.3-2L15 10v3a2 2 0 0 1-2 2A12 12 0 0 1 1 3a2 2 0 0 1 2-2z" fill="#fff"/></svg>555-318-2046
</div>
<div class="abs contact-row" style="top:3871px;font-size:15px">
  <svg width="16" height="13" viewBox="0 0 16 13" style="margin-top:3px"><path d="M0 5l8-5 8 5v8H0z" fill="#fff"/><path d="M0 5l8 5 8-5" fill="none" stroke="#1c1c1e" stroke-width="1.2"/></svg>info@orivaneenterprise.com
</div>
<div class="abs contact-row" style="top:3915px;font-size:13.5px;line-height:21px">
  <svg width="14" height="18" viewBox="0 0 14 18" style="margin-top:2px"><path d="M7 0a7 7 0 0 1 7 7c0 5-7 11-7 11S0 12 0 7a7 7 0 0 1 7-7z" fill="#fff"/><circle cx="7" cy="7" r="2.5" fill="#1c1c1e"/></svg>
  <span>12-58 Harlow Crescent,<br>Suite Brennic, Wendmoor Park<br>R7T 4N9</span>
</div>
<h4 class="abs" style="left:108px;top:3995px;font-size:19px;font-weight:300;color:var(--orange)">Useful Links</h4>
<div class="abs small-link" style="left:108px;top:4037px">Terms &amp; Conditions &nbsp;&nbsp;&nbsp;| &nbsp;&nbsp;Cookie policy</div>
<div class="abs small-link" style="left:108px;top:4058px">Privacy policy &nbsp;&nbsp;| &nbsp;&nbsp;Sitemap</div>
<div class="abs small-link" style="left:108px;top:4127px;color:#fff">©2022 Orivane Enterprise All Right Reserved.</div>

<h3 class="abs foot-title" style="left:528px;top:3752px">Request a Quote</h3>
<div class="abs field" style="top:3824px;height:35px">Your Name</div>
<div class="abs field" style="top:3874px;height:34px">Email</div>
<div class="abs field" style="top:3921px;height:35px">Phone</div>
<div class="abs field" style="top:3970px;height:122px">Type your message</div>
<a class="abs btn-solid" style="left:530px;top:4120px;width:105px;height:42px">Send</a>

<svg class="abs" style="left:1116px;top:3756px" width="58" height="58" viewBox="0 0 58 58"><rect x="12" y="12" width="34" height="34" transform="rotate(45 29 29)" fill="#ff6a25"/><path d="M29 35V23M25 27l4-4 4 4" fill="none" stroke="#fff" stroke-width="1.6"/></svg>

<a class="abs social" style="top:3996px" aria-label="Social profile one"><i></i></a>
<a class="abs social active" style="top:4040px" aria-label="Social profile two"><i></i></a>
<a class="abs social" style="top:4084px" aria-label="Social profile three"><i></i></a>
<a class="abs social" style="top:4128px" aria-label="Social profile four"><i></i></a>

</body>
</html>
```